Amber Lantern Cafe Business Card

We need a business card design for a new European Cafe. Main menu will be coffee and deserts.

Requirements
Must have
• Logo - 1 of the attached versions
Address - TBA (you can use 487 Morrow Ave Unit 9 for now)
Phone - TBA (you can use 555-238-4176 for now)

```html
<!DOCTYPE html>
<html lang="en">
<head>
<meta charset="utf-8">
<title>Amber Lantern Cafe – Business Card</title>
<link rel="stylesheet" href="https://fonts.googleapis.com/css2?family=Mulish:ital,wght@0,300;0,400;1,300&display=swap">
<style>
  :root {
    --paper: #ffffff;
    --ink: #111111;
    --panel: #0b1a1a;
    --panel-text: #f2f4f4;
  }
  html, body {
    margin: 0;
    padding: 0;
    width: 1200px;
    height: 686px;
    overflow: hidden;
    background: var(--paper);
  }
  .card {
    position: relative;
    width: 1200px;
    height: 686px;
    display: flex;
    font-family: "Mulish", "Helvetica Neue", Arial, sans-serif;
  }
  .brand-side {
    width: 498px;
    height: 100%;
    background: var(--paper);
    display: flex;
    flex-direction: column;
    align-items: center;
  }
  .brand-mark {
    width: 231px;
    height: 231px;
    margin-top: 143px;
    background: var(--ink);
    border-radius: 12px;
  }
  .brand-name {
    margin: 56px 0 0;
    font-weight: 400;
    color: var(--ink);
    text-align: center;
  }
  .brand-name-main {
    display: block;
    font-size: 57px;
    line-height: 60px;
    letter-spacing: -0.5px;
    white-space: nowrap;
  }
  .brand-name-sub {
    display: block;
    margin-top: 2px;
    font-size: 36px;
    line-height: 40px;
    letter-spacing: 3px;
  }
  .contact-side {
    flex: 1;
    height: 100%;
    background: var(--panel);
    color: var(--panel-text);
    position: relative;
    font-weight: 300;
  }
  .contact-block {
    position: absolute;
    right: 99px;
    text-align: right;
    margin: 0;
    white-space: nowrap;
  }
  .person {
    top: 140px;
  }
  .person-name {
    font-size: 45px;
    line-height: 54px;
    margin: 0;
    font-weight: 300;
  }
  .person-title {
    font-size: 41px;
    line-height: 54px;
    margin: 0;
    font-style: italic;
    font-weight: 300;
  }
  .address {
    top: 358px;
    font-size: 34px;
    line-height: 48px;
    font-style: normal;
  }
  .phone {
    top: 494px;
    font-size: 34px;
    line-height: 48px;
  }
</style>
</head>
<body>
  <div class="card">
    <section class="brand-side">
      <div class="brand-mark" aria-hidden="true"></div>
      <p class="brand-name">
        <span class="brand-name-main">Amber Lantern</span>
        <span class="brand-name-sub">Cafe</span>
      </p>
    </section>
    <section class="contact-side">
      <div class="contact-block person">
        <p class="person-name">Clara Whitfield</p>
        <p class="person-title">Manager</p>
      </div>
      <address class="contact-block address">
        487 Morrow Ave Unit 9,<br>
        Marlow Bay, Florida 34019
      </address>
      <p class="contact-block phone">(555) 238-4176</p>
    </section>
  </div>
</body>
</html>
```